Construction Company Facebook Banner

We are a small residential building company, building mostly new homes, renovations, extensions. our social media needs an uplift to look more professional.
I have no photos I wish to use in the banner as of yet however I have included the company logo, and the business card design which has some details.
I would like something simple but professional.
The banner does not need to have email, phone number, services provided etc. all of this is available on the facebook page itself. Something simple and clean please.
Industry/Entity Type
Construction
Requirements
Should not have
- Images of people, QR Code

```html
<!DOCTYPE html>
<html lang="en">
<head>
<meta charset="utf-8">
<title>Ridgeline Homes – Facebook Banner</title>
<link href="https://fonts.googleapis.com/css2?family=Poppins:wght@400;500;600;700;800&display=swap" rel="stylesheet">
<style>
  :root {
    --backdrop: #e3e0e0;
    --green: #2fb34a;
    --black: #0b0b0b;
    --white: #ffffff;
    --ink: #111111;
    --grey: #8a8d90;
  }
  * { margin: 0; padding: 0; box-sizing: border-box; }
  html, body {
    width: 1200px; height: 589px; overflow: hidden;
    background: var(--backdrop);
    font-family: "Poppins", sans-serif;
  }
  .banner {
    position: absolute; left: 78px; top: 89px;
    width: 1043px; height: 389px;
    background: var(--white);
    box-shadow: 0 6px 14px rgba(0,0,0,0.28);
    overflow: hidden;
  }
  .banner-shapes { position: absolute; inset: 0; }
  .brand {
    position: absolute; left: 34px; top: 62px;
    display: flex; flex-direction: column; align-items: center;
  }
  .brand-mark { width: 22px; height: 22px; background: var(--green); margin-bottom: 4px; }
  .brand-name { font-size: 17px; font-weight: 500; color: #3a3d40; letter-spacing: 0.5px; line-height: 1; }
  .brand-tagline { font-size: 5px; color: var(--grey); letter-spacing: 1.2px; margin-top: 2px; }
  .headline {
    position: absolute; left: 628px; width: 320px; text-align: center;
    font-weight: 800; line-height: 1; white-space: nowrap;
  }
  .headline-top { top: 35px; font-size: 27px; color: var(--ink); }
  .headline-main { top: 66px; font-size: 29px; color: var(--green); }
  .location { position: absolute; left: 654px; top: 108px; display: flex; align-items: center; gap: 6px; }
  .location-pill {
    background: var(--black); color: var(--white);
    border-radius: 8px; height: 28px; padding: 0 14px;
    display: flex; align-items: center;
    font-size: 19px; font-weight: 700; letter-spacing: 0.2px;
  }
  .location-pill .state { color: var(--green); margin-left: 5px; }
  .services-title {
    position: absolute; left: 628px; width: 320px; top: 147px; text-align: center;
    font-size: 13px; font-weight: 800; color: var(--ink); text-transform: uppercase;
  }
  .service {
    position: absolute; transform: translateX(-50%);
    display: flex; flex-direction: column; align-items: center;
    font-size: 13px; color: var(--ink); white-space: nowrap;
  }
  .service svg { width: 26px; height: 26px; margin-bottom: 2px; }
  .contact {
    position: absolute; top: 333px; display: flex; align-items: center; gap: 7px;
    color: var(--white); font-size: 19px; font-weight: 500;
  }
  .contact-icon {
    width: 17px; height: 17px; border-radius: 50%; background: var(--green);
    display: flex; align-items: center; justify-content: center;
  }
  .website {
    position: absolute; left: 676px; top: 330px; display: flex; align-items: center; gap: 12px;
    font-size: 24px; color: var(--ink); letter-spacing: 1.2px;
  }
  .website-dot { width: 14px; height: 14px; border-radius: 50%; background: var(--black); border: 4px solid var(--green); box-shadow: 0 0 0 2px var(--black); }
</style>
</head>
<body>
<div class="banner">
  <svg class="banner-shapes" viewBox="0 0 1043 389" width="1043" height="389">
    <defs>
      <linearGradient id="house-tones" x1="0" y1="0" x2="0" y2="1">
        <stop offset="0" stop-color="#c9cdd1"/>
        <stop offset="0.45" stop-color="#e6e6e4"/>
        <stop offset="1" stop-color="#9a8f86"/>
      </linearGradient>
      <linearGradient id="thumb-tones" x1="0" y1="0" x2="0" y2="1">
        <stop offset="0" stop-color="#cfd3d6"/>
        <stop offset="1" stop-color="#7d8a78"/>
      </linearGradient>
    </defs>
    <rect role="img" aria-label="Photo of a modern two-storey white home with dark roof" x="0" y="0" width="580" height="317" fill="url(#house-tones)"/>
    <polygon points="486,0 1043,0 1043,317 486,317" fill="var(--white)"/>
    <polygon points="450,0 486,0 486,150 560,140 1043,140 1043,317 470,317 520,230 430,0" fill="var(--green)"/>
    <polygon points="380,0 420,0 560,140 520,140" fill="var(--green)"/>
    <polygon role="img" aria-label="Photo of a patio roof structure" points="352,35 522,35 500,103 330,103" fill="url(#thumb-tones)" stroke="var(--white)" stroke-width="3"/>
    <polygon role="img" aria-label="Photo of a pergola over a garden" points="400,115 554,115 532,183 378,183" fill="url(#thumb-tones)" stroke="var(--white)" stroke-width="3"/>
    <polygon role="img" aria-label="Photo of a carport beside a garage" points="456,195 618,195 596,263 434,263" fill="url(#thumb-tones)" stroke="var(--white)" stroke-width="3"/>
    <polygon points="0,317 598,317 642,389 0,389" fill="var(--black)"/>
    <polygon points="598,317 622,317 662,389 642,389" fill="var(--green)"/>
  </svg>

  <div class="brand">
    <span class="brand-mark"></span>
    <span class="brand-name">RIDGELINE HOMES</span>
    <span class="brand-tagline">BUILDERS &amp; CARPENTERS</span>
  </div>

  <h1 class="headline headline-top">RESIDENTIAL LICENSED</h1>
  <h2 class="headline headline-main">BUILDERS &amp; CARPENTERS</h2>

  <div class="location">
    <svg width="18" height="24" viewBox="0 0 18 24"><path d="M9 0C4 0 0 4 0 9c0 6 9 15 9 15s9-9 9-15c0-5-4-9-9-9z" fill="var(--black)"/><circle cx="9" cy="9" r="3.5" fill="var(--white)"/></svg>
    <span class="location-pill">the Goldfields,<span class="state">WA</span></span>
  </div>

  <p class="services-title">We serve new homes renovation</p>

  <div class="service" style="left:662px; top:180px">
    <svg viewBox="0 0 26 26"><path d="M2 13h22v3a6 6 0 0 1-6 6H8a6 6 0 0 1-6-6z" fill="var(--black)"/><path d="M5 13V5a3 3 0 0 1 6 0" stroke="var(--black)" stroke-width="2" fill="none"/><circle cx="18" cy="8" r="2" fill="var(--green)"/></svg>
    Bathrooms
  </div>
  <div class="service" style="left:754px; top:180px">
    <svg viewBox="0 0 26 26"><path d="M3 22L16 9l3 3L6 25z" fill="var(--black)"/><path d="M14 4l8 8-2 2-8-8z" fill="var(--green)"/></svg>
    Carpentry
  </div>
  <div class="service" style="left:834px; top:180px">
    <svg viewBox="0 0 26 26"><path d="M13 2L1 11v13h24V11z" fill="var(--black)"/><rect x="7" y="13" width="12" height="11" fill="var(--white)"/><rect x="9" y="15" width="8" height="9" fill="var(--black)"/></svg>
    Sheds
  </div>
  <div class="service" style="left:916px; top:180px">
    <svg viewBox="0 0 26 26"><path d="M10 3L1 11v13h18V11z" fill="var(--black)"/><rect x="6" y="13" width="8" height="7" fill="var(--white)"/><rect x="19" y="14" width="6" height="10" fill="var(--green)"/></svg>
    Extensions
  </div>
  <div class="service" style="left:700px; top:236px">
    <svg viewBox="0 0 26 26"><path d="M13 2L1 10v14h24V10z" fill="var(--black)"/><rect x="5" y="12" width="16" height="12" fill="var(--white)"/><rect x="7" y="16" width="12" height="5" rx="2" fill="var(--black)"/></svg>
    Carports
  </div>
  <div class="service" style="left:789px; top:236px">
    <svg viewBox="0 0 26 26"><path d="M3 9L13 3l10 6z" fill="var(--black)"/><rect x="12" y="9" width="2" height="14" fill="var(--black)"/><rect x="7" y="15" width="12" height="2" fill="var(--black)"/><rect x="2" y="14" width="2" height="9" fill="var(--black)"/><rect x="22" y="14" width="2" height="9" fill="var(--black)"/></svg>
    Patios
  </div>
  <div class="service" style="left:878px; top:236px">
    <svg viewBox="0 0 26 26"><path d="M13 2L1 11v13h24V11z" fill="var(--black)"/><path d="M8 20l10-8M8 12l10 8" stroke="var(--white)" stroke-width="2.5"/></svg>
    Renovations
  </div>

  <div class="contact" style="left:44px">
    <span class="contact-icon"><svg width="10" height="10" viewBox="0 0 10 10"><path d="M2 1l2 2-1 1.5a6 6 0 0 0 2.5 2.5L7 6l2 2-1.5 1.5C4 9 1 6 .5 2.5z" fill="var(--black)"/></svg></span>
    +61 400 000 123
  </div>
  <div class="contact" style="left:258px">
    <span class="contact-icon"><svg width="10" height="8" viewBox="0 0 10 8"><rect x="0" y="0" width="10" height="8" rx="1" fill="var(--black)"/><path d="M0.5 1l4.5 3.5L9.5 1" stroke="var(--green)" fill="none"/></svg></span>
    admin@ridgeline-homes.com
  </div>
  <div class="website">
    <span class="website-dot"></span>
    ridgeline-homes.com
  </div>
</div>
</body>
</html>
```